Modern labels for Murlane products

We need a new design of our labels for the product “Murlane” (https://www.murlane-example.eu/#) . The reason why we want to change our labels is to get a modern and more advanced look of our product. We also want to create a unique product that is attractive for our customers, even if the product are used in hospitals and healthcare centers for collecting dangerous waste.

There is three sizes of labels (55x95, 90x95, 170x95 mm) for different boxes, but the label will contain similar information. There are certain requirements and factors from regulations/standards that you need to follow when you create the new layout. But it’s up to you to change the design. You can work with background, fonts, effects, colors, structure, pattern, new symbols, logotype etc. The label could be any color, but the container will stay yellow so they have to look good together.

Keywords: Elegant, modern, functional, attractive, exclusive

Target Market(s)

Hospitals and healthcare centers

Industry/Entity Type

Product

Font styles to use
Serif
Sans Serif

Colors

Designer to choose colors to be used in the design.

Requirements
Must have
• Requirements for the regulations ADR UN3291 and ISO 23907 (PDF).
• * Symbol for danger waste
• * Filling level
• * "Danger"
• * Symbol for no second use
• * Symbol for manufaturer
• * Referencenumber
• * Text "”Clinical waste, Unspecified, N.O.S.”"
• * Area for series, certification, size and useful capacity
• * Area for Illustrations.
• * Text “Autoclavable at 134 c”, “Do not force closure” and “Do not overfill”.
• * Text for certification ”UN 3291 1H2/Y0,3/S/YR/N/QVK7148B”
• Three different sizes (55x95, 90x95, 170x95).
• More info in PDF "3kravspecifikation"
Nice to have
• A modern, elegant, advanced look of our label.
Should not have
• The information must be clear and readable, not too decorative/handwriting fonts.

```html
<!DOCTYPE html>
<html lang="en">
<head>
<meta charset="utf-8">
<title>Murlane clinical waste label</title>
<link rel="stylesheet" href="https://fonts.googleapis.com/css2?family=Archivo+Black&family=Open+Sans:wght@400;600;700;800&display=swap">
<style>
  :root {
    --orange: #f7941d;
    --yellow: #efe920;
    --black: #000000;
    --white: #ffffff;
    --navy: #2e2c6c;
    --ink: #1a1a1a;
  }
  * { margin: 0; padding: 0; box-sizing: border-box; }
  html, body { width: 1200px; height: 1138px; overflow: hidden; }
  body { background: var(--orange); font-family: "Open Sans", Arial, sans-serif; color: var(--black); }
  .label { position: relative; width: 1200px; height: 1138px; overflow: hidden; }
  .abs { position: absolute; }

  .yellow-field { left: 0; top: 0; width: 1200px; height: 1138px; }

  .fill-level-band { left: 0; top: 0; width: 1200px; height: 94px; background: var(--orange); }
  .fill-level-title { left: 0; top: 0; width: 1200px; height: 94px; line-height: 94px; text-align: center;
    font-weight: 800; font-size: 46px; letter-spacing: 1px; }
  .chevrons { top: 32px; }

  .danger-title { left: 0; top: 86px; width: 1200px; text-align: center; font-family: "Archivo Black", "Arial Black", sans-serif;
    font-size: 132px; line-height: 150px; letter-spacing: 0; transform: scaleX(0.82); transform-origin: 600px 0; }
  .waste-type { left: 0; top: 214px; width: 1200px; text-align: center; font-weight: 700; font-size: 44px; line-height: 56px; }

  .hazard-diamond { left: 34px; top: 288px; }
  .no-reuse { left: 30px; top: 288px; }
  .un-number { left: 0; width: 405px; top: 632px; text-align: center; font-weight: 800; font-size: 52px; line-height: 64px; }
  .un-code { left: 0; width: 405px; top: 696px; text-align: center; font-weight: 700; font-size: 21px; letter-spacing: 0.5px; }

  .spec-tag { left: 414px; height: 36px; line-height: 36px; padding: 0 8px; background: var(--black); color: var(--white);
    font-weight: 700; font-size: 20px; letter-spacing: 1px; }
  .spec-value { left: 420px; font-weight: 700; font-size: 20px; letter-spacing: 1px; line-height: 26px; }

  .illustration-area { background: var(--white); }

  .warnings { top: 769px; font-weight: 700; font-size: 21px; letter-spacing: 1.9px; color: var(--white); line-height: 32px; }
  .warning-dot { width: 14px; height: 14px; border-radius: 50%; background: var(--white); top: 779px; }

  .info-panel { left: 12px; top: 836px; width: 1176px; height: 286px; background: var(--white); border-radius: 8px; }
  .fill-in-box { left: 36px; top: 854px; width: 702px; height: 248px; background: var(--yellow); border: 2px solid var(--black); border-radius: 18px; }
  .field-label { left: 52px; font-weight: 700; font-size: 21px; color: var(--navy); letter-spacing: 0.5px; line-height: 30px; }
  .field-icon { left: 228px; }
  .field-input { left: 292px; width: 423px; height: 49px; background: var(--white); }

  .brand-name { left: 822px; top: 862px; font-weight: 700; font-size: 50px; line-height: 64px; color: var(--navy); }
  .maker-line { left: 822px; font-size: 26px; line-height: 34px; color: var(--ink); }
  .maker-web { font-weight: 700; color: var(--black); }
  .factory-icon { left: 838px; top: 1036px; }
</style>
</head>
<body>
<main class="label">
  <svg class="abs yellow-field" width="1200" height="1138" aria-hidden="true">
    <polygon points="0,94 1200,94 1200,778 1152,744 48,744 0,778" fill="var(--yellow)"/>
  </svg>

  <header>
    <div class="abs fill-level-band"></div>
    <svg class="abs chevrons" style="left:10px" width="362" height="30" aria-hidden="true">
      <defs>
        <pattern id="chev-left" width="30" height="30" patternUnits="userSpaceOnUse">
          <polyline points="22,3 10,15 22,27" fill="none" stroke="var(--black)" stroke-width="6"/>
        </pattern>
      </defs>
      <rect width="362" height="30" fill="url(#chev-left)"/>
    </svg>
    <svg class="abs chevrons" style="left:828px" width="362" height="30" aria-hidden="true">
      <defs>
        <pattern id="chev-right" width="30" height="30" patternUnits="userSpaceOnUse">
          <polyline points="8,3 20,15 8,27" fill="none" stroke="var(--black)" stroke-width="6"/>
        </pattern>
      </defs>
      <rect width="362" height="30" fill="url(#chev-right)"/>
    </svg>
    <h2 class="abs fill-level-title">FILLING LEVEL</h2>
  </header>

  <h1 class="abs danger-title">DANGER</h1>
  <p class="abs waste-type">CLINICAL WASTE, Unspecified, N.O.S.</p>

  <svg class="abs hazard-diamond" width="340" height="340" viewBox="0 0 340 340" role="img" aria-label="Class 6 infectious substance hazard diamond">
    <polygon points="170,0 340,170 170,340 0,170" fill="var(--black)"/>
    <polygon points="170,7 333,170 170,333 7,170" fill="var(--white)"/>
    <polygon points="170,14 326,170 170,326 14,170" fill="var(--black)"/>
    <polygon points="170,17 323,170 170,323 17,170" fill="var(--white)"/>
    <g transform="translate(170,112)">
      <circle cx="0" cy="-22" r="27" fill="var(--black)"/>
      <circle cx="-22" cy="14" r="27" fill="var(--black)"/>
      <circle cx="22" cy="14" r="27" fill="var(--black)"/>
      <circle cx="0" cy="-30" r="20" fill="var(--white)"/>
      <circle cx="-28" cy="18" r="20" fill="var(--white)"/>
      <circle cx="28" cy="18" r="20" fill="var(--white)"/>
      <circle cx="0" cy="3" r="20" fill="none" stroke="var(--black)" stroke-width="7"/>
      <circle cx="0" cy="3" r="7" fill="var(--white)"/>
    </g>
    <text x="170" y="283" text-anchor="middle" font-family="Arial, sans-serif" font-size="30">6</text>
  </svg>

  <svg class="abs no-reuse" width="72" height="72" viewBox="0 0 72 72" role="img" aria-label="Do not reuse">
    <circle cx="36" cy="36" r="32" fill="none" stroke="var(--black)" stroke-width="4"/>
    <text x="36" y="49" text-anchor="middle" font-family="Open Sans, Arial, sans-serif" font-weight="700" font-size="38">2</text>
    <line x1="13" y1="59" x2="59" y2="13" stroke="var(--black)" stroke-width="4"/>
  </svg>

  <p class="abs un-number">UN 3291</p>
  <p class="abs un-code">1H2/Y0,3/S/YR/N/QVK7148B</p>

  <section class="product-specs">
    <span class="abs spec-tag" style="top:310px">SERIES</span>
    <span class="abs spec-value" style="top:354px">ARDEN</span>
    <span class="abs spec-tag" style="top:412px">CERTIFICATION</span>
    <span class="abs spec-value" style="top:456px">ISO23907:2012</span>
    <span class="abs spec-tag" style="top:510px">SIZE</span>
    <span class="abs spec-value" style="top:554px">2,2 L</span>
    <span class="abs spec-tag" style="top:612px">USEFUL CAPACITY</span>
    <span class="abs spec-value" style="top:656px">1,76 L</span>
  </section>

  <div class="abs illustration-area" style="left:674px;top:284px;width:220px;height:208px"></div>
  <div class="abs illustration-area" style="left:672px;top:514px;width:220px;height:206px"></div>
  <div class="abs illustration-area" style="left:910px;top:284px;width:271px;height:436px"></div>

  <p class="abs warnings" style="left:90px">AUTOCLAVABLE AT 134 C</p>
  <span class="abs warning-dot" style="left:434px"></span>
  <p class="abs warnings" style="left:491px">DO NOT FORCE CLOSURE</p>
  <span class="abs warning-dot" style="left:834px"></span>
  <p class="abs warnings" style="left:897px">DO NOT OVERFILL</p>

  <section class="abs info-panel"></section>
  <div class="abs fill-in-box"></div>

  <span class="abs field-label" style="top:889px">PLACE/CLINIC</span>
  <svg class="abs field-icon" style="top:880px" width="44" height="44" viewBox="0 0 44 44" aria-hidden="true">
    <path d="M4 18 L22 4 L40 18 V42 H4 Z" fill="var(--navy)"/>
    <path d="M2 18 L22 2 L42 18" fill="none" stroke="var(--navy)" stroke-width="3"/>
    <rect x="18" y="19" width="8" height="18" fill="var(--white)"/>
    <rect x="13" y="24" width="18" height="8" fill="var(--white)"/>
  </svg>
  <div class="abs field-input" style="top:882px"></div>

  <span class="abs field-label" style="top:962px">DEPARTMENT</span>
  <svg class="abs field-icon" style="top:954px" width="44" height="46" viewBox="0 0 44 46" aria-hidden="true">
    <rect x="15" y="2" width="14" height="12" fill="var(--navy)"/>
    <path d="M22 14 V24 M7 24 H37 M7 24 V32 M37 24 V32 M22 24 V32" stroke="var(--navy)" stroke-width="3" fill="none"/>
    <rect x="1" y="32" width="12" height="12" fill="var(--navy)"/>
    <rect x="16" y="32" width="12" height="12" fill="var(--navy)"/>
    <rect x="31" y="32" width="12" height="12" fill="var(--navy)"/>
  </svg>
  <div class="abs field-input" style="top:950px"></div>

  <span class="abs field-label" style="top:1032px">SEALING DATE</span>
  <svg class="abs field-icon" style="top:1024px" width="44" height="46" viewBox="0 0 44 46" aria-hidden="true">
    <rect x="3" y="7" width="38" height="36" rx="3" fill="none" stroke="var(--navy)" stroke-width="4"/>
    <rect x="3" y="7" width="38" height="9" fill="var(--navy)"/>
    <rect x="11" y="2" width="5" height="10" fill="var(--navy)"/>
    <rect x="28" y="2" width="5" height="10" fill="var(--navy)"/>
    <g fill="var(--navy)">
      <rect x="10" y="21" width="6" height="5"/><rect x="19" y="21" width="6" height="5"/><rect x="28" y="21" width="6" height="5"/>
      <rect x="10" y="30" width="6" height="5"/><rect x="19" y="30" width="6" height="5"/><rect x="28" y="30" width="6" height="5"/>
    </g>
  </svg>
  <div class="abs field-input" style="top:1022px"></div>

  <p class="abs brand-name">Murlane</p>
  <p class="abs maker-line" style="top:932px">Lindhaven, Sweden</p>
  <p class="abs maker-line maker-web" style="top:964px">www.murlane-example.eu</p>
  <p class="abs maker-line" style="top:996px">Ref:&nbsp; xxxxx-xx-xx-xx</p>
  <svg class="abs factory-icon" width="54" height="60" viewBox="0 0 54 60" role="img" aria-label="Manufacturer">
    <path d="M0 60 V20 L14 30 V20 L28 30 V20 L38 27 V0 H48 V60 Z" fill="var(--black)"/>
  </svg>
</main>
</body>
</html>
```